Trade Alert Service needs Vistrel thumbnail / channel design

I'm about to set up a Vistrel channel which gives real-time trade alerts to earn passive income. I'm looking for a Vistrel channel design to include thumbnail and other associated visuals for the channel.
The trade alerts will be focused around selling cash-secured put options on US equities, and directed at people who want investing advice / tips for getting out of the rat race. I'd like the theme to be somewhat serious / credible, without too many eye-popping neon colours like all the other cheap trade alert videos / day trading videos on Vistrel. Happy for you to use your experience if you think otherwise though, as you're the designer, not me!

Target Market(s)

Option Traders, Value Investors, People who want passive income

Industry/Entity Type

Finance

Logo Text

Calm Meadow Wealth Notes

Requirements
Must have
• All relevant Vistrel visuals so that I can upload them to the Vistrel channel - all visuals required by Vistrel Studio upload within the channel creation page.
A logo so that I can append it to Powerpoint presentations
Nice to have
• A blank Powerpoint slide template showing the logo would be great in chosen colour scheme

```html
<!DOCTYPE html>
<html lang="en">
<head>
<meta charset="utf-8">
<title>Trading and Investing Our Way to Financial Freedom</title>
<link href="https://fonts.googleapis.com/css2?family=Montserrat:ital,wght@1,800;1,900&display=swap" rel="stylesheet">
<style>
  :root {
    --page: #ffffff;
    --blue: #4a6db3;
    --blue-deep: #1f3a78;
    --navy: #13234a;
    --orange: #e8840f;
    --white: #ffffff;
    --photo-dark: #1c1a1d;
    --photo-warm: #3a2a22;
    --photo-table: #cfd1d6;
  }
  html, body {
    margin: 0;
    width: 1200px;
    height: 1000px;
    overflow: hidden;
    background: var(--page);
  }
  .thumbnail {
    position: absolute;
    left: 70px;
    top: 195px;
    width: 1043px;
    height: 585px;
    overflow: hidden;
    box-shadow: 6px 12px 22px rgba(0,0,0,0.35);
    font-family: "Montserrat", sans-serif;
    font-style: italic;
  }
  .trading-photo {
    position: absolute;
    inset: 0;
    background:
      linear-gradient(160deg, transparent 45%, var(--photo-table) 46%, #e6e7ea 70%, #b9bcc3 100%),
      linear-gradient(120deg, var(--photo-warm) 0%, var(--photo-dark) 60%, #0f0f12 100%);
  }
  .shapes {
    position: absolute;
    inset: 0;
  }
  .headline {
    position: absolute;
    left: 66px;
    margin: 0;
    font-weight: 900;
    text-transform: uppercase;
    letter-spacing: 0.5px;
    line-height: 1;
    white-space: nowrap;
  }
  .headline-white { top: 88px; font-size: 65px; color: var(--white); }
  .headline-orange { top: 150px; font-size: 65px; color: var(--orange); }
  .tag-navy {
    position: absolute;
    left: 56px;
    top: 230px;
    width: 297px;
    height: 49px;
    margin: 0;
    background: var(--navy);
    color: var(--white);
    font-weight: 800;
    font-size: 36px;
    line-height: 49px;
    text-align: center;
    white-space: nowrap;
  }
  .band-label {
    position: absolute;
    left: 74px;
    margin: 0;
    color: var(--white);
    font-weight: 900;
    font-size: 57px;
    white-space: nowrap;
  }
  .band-financial { top: 295px; height: 80px; line-height: 80px; }
  .band-freedom { top: 391px; height: 76px; line-height: 76px; }
</style>
</head>
<body>
  <section class="thumbnail">
    <div class="trading-photo" role="img" aria-label="Photo of a hand on a laptop keyboard beside a tablet and smartphone showing trading charts on a desk"></div>

    <svg class="shapes" width="1043" height="585" viewBox="0 0 1043 585" aria-hidden="true">
      <defs>
        <linearGradient id="panelShade" x1="0" y1="0" x2="0.4" y2="1">
          <stop offset="0" stop-color="#4d71b8"/>
          <stop offset="0.45" stop-color="#2b4a8c"/>
          <stop offset="0.7" stop-color="#1f3a78"/>
          <stop offset="1" stop-color="#4a6db3"/>
        </linearGradient>
      </defs>
      <polygon points="0,0 620,0 705,175 555,585 0,585" fill="url(#panelShade)"/>
      <polygon points="0,330 520,200 560,220 0,410" fill="#4a6db3" opacity="0.55"/>
      <polygon points="508,0 575,0 705,175" fill="var(--orange)"/>
      <polygon points="56,295 408,295 440,375 56,375" fill="var(--orange)"/>
      <polygon points="56,391 408,391 440,467 56,467" fill="var(--orange)"/>
    </svg>

    <h1 class="headline headline-white">Trading and</h1>
    <p class="headline headline-orange">Investing</p>
    <p class="tag-navy">OUR WAY TO</p>
    <p class="band-label band-financial">FINANCIAL</p>
    <p class="band-label band-freedom">FREEDOM</p>
  </section>
</body>
</html>
```